Veltrano - Mechanic/Collision Center Business Card

We're looking for a business card design for our mechanic/ collision repair shop.

Can be with colours or monochromatic.

See the attached files.

Many thanks

```html
<!DOCTYPE html>
<html lang="en">
<head>
<meta charset="utf-8">
<title>Veltrano – Business Card</title>
<link href="https://fonts.googleapis.com/css2?family=Audiowide&family=Montserrat:wght@400;500&display=swap" rel="stylesheet">
<style>
  :root {
    --backdrop: #2a2a2c;
    --card-dark: #0b0b0d;
    --card-light: #ffffff;
    --brand-blue: #1a78c2;
    --icon-blue: #2a9fe0;
    --ink: #1c1c1e;
    --ink-soft: #3a3a3c;
    --white: #ffffff;
  }
  * { margin: 0; padding: 0; box-sizing: border-box; }
  html, body { width: 1200px; height: 900px; overflow: hidden; }
  body {
    background: var(--backdrop);
    display: flex;
    align-items: center;
    justify-content: center;
    gap: 50px;
    font-family: "Montserrat", sans-serif;
  }
  .card {
    position: relative;
    width: 540px;
    height: 310px;
    border-radius: 18px;
    box-shadow: 0 14px 30px rgba(0,0,0,.5);
  }
  .card--front {
    background: var(--card-dark);
    display: flex;
    align-items: center;
    justify-content: center;
  }
  .card--back { background: var(--card-light); }

  .wordmark {
    font-family: "Audiowide", sans-serif;
    text-transform: uppercase;
    letter-spacing: 1px;
    display: flex;
    align-items: center;
    gap: 12px;
  }
  .wordmark__dot {
    width: 18px; height: 18px; border-radius: 50%;
    background: currentColor;
  }
  .card--front .wordmark { color: var(--white); font-size: 46px; }
  .tagline {
    position: absolute;
    left: 0; right: 0; top: 190px;
    text-align: center;
    font-family: "Audiowide", sans-serif;
    font-size: 13px;
    color: var(--white);
    letter-spacing: 2px;
  }

  .company-name {
    position: absolute;
    left: 34px; top: 74px;
    font-family: "Audiowide", sans-serif;
    font-size: 22px;
    color: var(--brand-blue);
    text-transform: uppercase;
    letter-spacing: 1.5px;
  }
  .card--back .wordmark {
    position: absolute;
    right: 30px; top: 30px;
    color: var(--ink);
    font-size: 26px;
    gap: 8px;
  }
  .card--back .wordmark__dot { width: 12px; height: 12px; color: var(--brand-blue); background: var(--brand-blue); }
  .card--back .est {
    position: absolute;
    right: 30px; top: 68px;
    font-family: "Audiowide", sans-serif;
    font-size: 10px;
    color: var(--ink);
    letter-spacing: 1.5px;
  }

  .contact {
    position: absolute;
    left: 34px; bottom: 30px;
    list-style: none;
    font-size: 14px;
    line-height: 1.45;
    color: var(--ink-soft);
  }
  .contact__item { display: flex; align-items: center; gap: 8px; }
  .contact__item svg { width: 14px; height: 14px; flex: none; }
  .contact__plain { padding-left: 0; }
  .contact__gap { margin-top: 4px; }

  .card-notch {
    position: absolute;
    left: 0; bottom: 40px;
    width: 14px; height: 70px;
    background: var(--backdrop);
    border-radius: 0 8px 8px 0;
  }
</style>
</head>
<body>

  <section class="card card--front" aria-label="Card front">
    <div class="wordmark"><span class="wordmark__dot"></span>Veltrano</div>
    <div class="tagline">EST. 1979</div>
  </section>

  <section class="card card--back" aria-label="Card back">
    <h1 class="company-name">Veltrano, LDA</h1>

    <div class="wordmark"><span class="wordmark__dot"></span>Veltrano</div>
    <div class="est">EST. 1979</div>

    <ul class="contact">
      <li class="contact__plain">Adress: Rua das Oficinas, 42</li>
      <li class="contact__plain">Postal code: 1100-214 Lisboa</li>
      <li class="contact__item contact__gap">
        <svg viewBox="0 0 16 16" aria-hidden="true"><path fill="var(--icon-blue)" d="M3 1h3l1.5 4-2 1.2a9 9 0 0 0 4.3 4.3L11 8.5l4 1.5v3a2 2 0 0 1-2 2A12 12 0 0 1 1 3a2 2 0 0 1 2-2z"/></svg>
        +351 215550147
      </li>
      <li class="contact__item">
        <svg viewBox="0 0 16 16" aria-hidden="true"><rect x="1" y="3" width="14" height="10" rx="1" fill="var(--icon-blue)"/><path d="M1.5 3.5 8 9l6.5-5.5" fill="none" stroke="#fff" stroke-width="1.3"/></svg>
        geral@veltrano.pt
      </li>
      <li class="contact__item">
        <svg viewBox="0 0 16 16" aria-hidden="true"><rect x="1" y="1" width="14" height="14" rx="2" fill="var(--icon-blue)"/></svg>
        www.veltrano-auto.pt
      </li>
    </ul>

    <div class="card-notch"></div>
  </section>

</body>
</html>
```